New Label Design Project Velora Hair Care Product Line

The brand name is Velora Hair Care. I would like the designs to stand out and that it will compliment cobalt blue jars and bottles (4oz and 8oz). I would like for the designs to be elegant, attractive, eye catching with a goddess feel to it (the name Velora is Greek) and have enough to list product information on them. I have attached the product details to be put on the labels. I hope this helps. I appreciate your time.
Doreen Whitcombe

Target Market(s)

Hair and Beauty industry

Industry/Entity Type

Hair Care Product

Colors
33a6d7
faa54b
acd037

Requirements
Must have
• Brand colors are Blue, green, and orange, must be able to fit label sizes indicated in the attachment
Nice to have
• creative graphic designs :)

```html
<!DOCTYPE html>
<html lang="en">
<head>
<meta charset="utf-8">
<title>Velora Hair Care – Luminance Moisturizing Mint Shampoo</title>
<link rel="stylesheet" href="https://fonts.googleapis.com/css2?family=Merriweather:wght@400;700;900&family=Great+Vibes&display=swap">
<style>
  :root {
    --backdrop: #ececec;
    --brand-blue: #5aaed6;
    --brand-orange: #f6a24a;
    --ink: #1e1e1e;
    --paper: #fbfdf6;
    --paper-mid: #eef5dc;
    --paper-green: #d2e79f;
    --mint-dark: #2f7d1f;
    --mint-mid: #4aa532;
    --white: #ffffff;
  }
  * { margin: 0; padding: 0; box-sizing: border-box; }
  html, body { width: 1200px; height: 614px; overflow: hidden; background: var(--backdrop); }
  .canvas {
    position: relative; width: 1200px; height: 614px; overflow: hidden;
    background: var(--backdrop);
    font-family: "Merriweather", Georgia, serif; color: var(--ink);
  }

  .label {
    position: absolute; left: 349px; top: 0; width: 502px; height: 614px;
    background: linear-gradient(180deg, var(--paper) 0%, var(--paper) 30%, var(--paper-mid) 62%, var(--paper-green) 100%);
    overflow: hidden;
  }
  .label-header { position: absolute; left: 0; top: 0; width: 502px; height: 150px; }
  .brand-name {
    position: absolute; left: 0; top: 58px; width: 502px; text-align: center;
    font-weight: 400; font-size: 30px; letter-spacing: 1px; color: var(--white);
    white-space: nowrap;
  }
  .tagline {
    position: absolute; left: 0; top: 154px; width: 502px; text-align: center;
    font-size: 12.4px; line-height: 18px; white-space: nowrap;
  }
  .product-name {
    position: absolute; left: 0; top: 196px; width: 502px; text-align: center;
    font-weight: 900; font-size: 64px; line-height: 1.2; color: var(--brand-orange);
    text-shadow: 1px 2px 2px rgba(0,0,0,0.25); white-space: nowrap;
  }
  .product-type { position: absolute; left: 22px; top: 288px; width: 290px; font-weight: 400; }
  .product-type .script {
    display: block; font-family: "Great Vibes", cursive; font-weight: 400;
    font-size: 60px; line-height: 60px; white-space: nowrap;
  }
  .product-type .plain {
    display: block; font-size: 28px; line-height: 32px; font-weight: 400; white-space: nowrap;
  }
  .product-type .mint { margin-left: 60px; }
  .product-type .shampoo { margin-left: 26px; }
  .herb-art {
    position: absolute; left: 226px; top: 298px; width: 256px; height: 190px;
    border-radius: 50% 45% 50% 40%;
    background: radial-gradient(ellipse at 50% 50%, var(--mint-mid) 0%, var(--mint-dark) 45%, rgba(47,125,31,0) 72%);
  }
  .description {
    position: absolute; left: 0; top: 503px; width: 502px; text-align: center;
    font-size: 12.4px; line-height: 18.5px; white-space: nowrap;
  }
  .size {
    position: absolute; left: 0; top: 570px; width: 502px; text-align: center;
    font-weight: 700; font-size: 18px;
  }
</style>
</head>
<body>
<main class="canvas">
  <section class="label">
    <svg class="label-header" viewBox="0 0 502 150" aria-hidden="true">
      <path d="M0 0 H502 V3 Q251 14 0 3 Z" fill="var(--brand-orange)"/>
      <path d="M0 5 Q251 16 502 5 V138 Q300 128 0 146 Z" fill="var(--brand-blue)"/>
      <path d="M0 146 Q300 128 502 138" stroke="var(--brand-orange)" stroke-width="3" fill="none"/>
    </svg>
    <div class="brand-name">Velora Hair Care</div>
    <p class="tagline">A natural approach to healthy hair care designed for<br>chemically treated and non chemically treated hair.</p>
    <h1 class="product-name">Luminance</h1>
    <h2 class="product-type">
      <span class="script">Moisturizing</span>
      <span class="plain mint">Mint</span>
      <span class="plain shampoo">Shampoo</span>
    </h2>
    <div class="herb-art" role="img" aria-label="Sprig of fresh green peppermint leaves"></div>
    <p class="description">Cleansing shampoo that will leave hair moisturized<br>without stripping the hair. Infused with peppermint to<br>leave the scalp feeling refreshed</p>
    <p class="size">8 oz</p>
  </section>
</main>
</body>
</html>
```